Business Card Design

I need a Business Card that will catch the attention that will not get thrown in a Drawer. I have 23 companies I use for Auto, Home, Life, and Business Insurance. I make sure that people have the best coverage for the $ spent.

Industry/Entity Type

Business

Contact Information for Business Card

Dorlin Insurance Agency, Inc., Marcus Helgren, 4375 West Tamber Lane Alvenport, Westmark 45192 555-281-7496, www.dorlinagency.example, Kindra, Netwerk, Plazio

```html
<!DOCTYPE html>
<html lang="en">
<head>
<meta charset="utf-8">
<title>Dorlin Insurance Agency – Business Card</title>
<link rel="stylesheet" href="https://fonts.googleapis.com/css2?family=Marcellus&family=Open+Sans:ital,wght@0,400;1,400&display=swap">
<style>
  :root {
    --slate: #5b5a55;
    --charcoal: #2b2b29;
    --rule-grey: #b3b3b3;
    --paper: #ffffff;
    --ink: #111111;
    --orange: #fe5a10;
    --panel-black: #000000;
    --social-blue: #2a63b8;
    --muted-white: #e4e4e4;
  }
  * { margin: 0; padding: 0; box-sizing: border-box; }
  html, body { width: 1200px; height: 704px; overflow: hidden; background: var(--paper); }
  .card { position: relative; width: 1200px; height: 704px; overflow: hidden; background: var(--paper); }

  .header-band { position: absolute; left: 0; top: 0; width: 1200px; height: 149px; background: var(--slate); }
  .agency-name {
    position: absolute; left: 64px; top: 50px;
    font-family: "Marcellus", serif; font-weight: 400; font-size: 66px; line-height: 1;
    color: var(--paper); letter-spacing: 0.3px; white-space: nowrap;
  }
  .agency-slogan {
    position: absolute; right: 63px; top: 110px;
    font-family: "Open Sans", sans-serif; font-style: italic; font-size: 20px;
    color: var(--muted-white); white-space: nowrap;
  }

  .promise-band {
    position: absolute; left: 0; top: 149px; width: 1200px; height: 39px;
    background: var(--charcoal);
    display: flex; align-items: center; justify-content: center;
  }
  .promise-text {
    font-family: "Open Sans", sans-serif; font-style: italic; font-size: 21.3px;
    color: var(--paper); white-space: nowrap; transform: translateX(2px);
  }

  .divider { position: absolute; left: 0; width: 1200px; height: 11px; background: var(--rule-grey); }
  .divider--top { top: 188px; }
  .divider--bottom { top: 530px; }

  .agent-name {
    position: absolute; left: 119px; top: 305px;
    font-family: "Marcellus", serif; font-size: 106px; line-height: 1;
    color: var(--ink); white-space: nowrap;
  }

  .coverage-panel { position: absolute; left: 945px; top: 199px; width: 192px; height: 331px; background: var(--panel-black); }
  .coverage-rule { position: absolute; left: 37px; width: 131px; height: 4.5px; background: var(--paper); }
  .coverage-item {
    position: absolute; left: 0; width: 192px; text-align: center;
    font-family: "Marcellus", serif; font-size: 35px; line-height: 1; color: var(--paper);
  }

  .contact-band { position: absolute; left: 0; top: 541px; width: 1200px; height: 163px; background: var(--orange); }
  .contact-details {
    position: absolute; left: 63px; top: 43px;
    font-family: "Open Sans", sans-serif; font-size: 20.5px; line-height: 29px; color: var(--ink);
  }
  .social-links {
    position: absolute; right: 63px; top: 65px;
    display: flex; gap: 14px; align-items: center;
    font-family: "Open Sans", sans-serif; font-size: 16px; color: var(--ink);
  }
  .social-link { display: flex; align-items: center; gap: 6px; }
  .social-mark { width: 14px; height: 14px; background: var(--social-blue); }
</style>
</head>
<body>
<div class="card">
  <div class="header-band">
    <div class="agency-name">Dorlin Insurance Agency, Inc.</div>
    <div class="agency-slogan">The Insurance specialist</div>
  </div>

  <div class="promise-band">
    <p class="promise-text">As independent agents, we don't work for the insurance company; we work for you.</p>
  </div>

  <div class="divider divider--top"></div>

  <div class="agent-name">Marcus Helgren</div>

  <div class="coverage-panel">
    <div class="coverage-rule" style="top:26px"></div>
    <div class="coverage-item" style="top:44px">Auto</div>
    <div class="coverage-rule" style="top:95px"></div>
    <div class="coverage-item" style="top:108px">Home</div>
    <div class="coverage-rule" style="top:159px"></div>
    <div class="coverage-item" style="top:173px">Live</div>
    <div class="coverage-rule" style="top:221px"></div>
    <div class="coverage-item" style="top:236px">Business</div>
    <div class="coverage-rule" style="top:292px"></div>
  </div>

  <div class="divider divider--bottom"></div>

  <div class="contact-band">
    <div class="contact-details">
      <div class="contact-address">Address: 4375 West Tamber Lane Alvenport, Westmark 45192</div>
      <div class="contact-phone">Phone: 555-281-7496</div>
    </div>
    <div class="social-links">
      <span class="social-link"><span class="social-mark"></span>Kindra</span>
      <span class="social-link"><span class="social-mark"></span>Plazio</span>
      <span class="social-link"><span class="social-mark"></span>Netwerk</span>
    </div>
  </div>
</div>
</body>
</html>
```